Buch-/E-Book-Cover Autobiographische Kurzgeschichten
Tolle Umsetzung meiner Vorgaben. Eigeninitiative gezeigt, das gefällt mir. Sehr geduldig wegen weiterer, kleiner Änderungen. Die Zusammenarbeit gefiel mir sehr gut
Zielgruppe
Ich vermarkte mein Buch selbst. Zielgruppe sind Frauen und Männer, die leichte Lektüre mit Humor und Lebenserfahrung lesen wollen.
Aufgabenstellung
Das Buch hat den Titel 'Sturmflut im Herbstlicht'.
Der Inhalt sind autobiographische Kurzgeschichten.
Erst verwitwet wagte ich einen Blick über den Zaun. Und tatsächlich war dort das Gras grüner, die Wiese enthielt lebenswichtige Kräuter und bunte Blumen. Da wollte ich hier, nur wie? Ich hatte „Zäune überwinden“ nicht gelernt. Versuch und Irrtum, Feldforschung, Kampf mit mir selbst, ein nie Aufgeben führten mich zum Erfolg, auf die andere Seite. Und die Wiese hält, was sie versprach. Da hatten sich doch der Witwentröster, das Datingportal, der Escort, den ich nicht mit aufs Zimmer nahm, die Aktfotos und und und gelohnt.
Meine autobiographischen Geschichten sind wie ein gutes Parfum mit Kopf-, Herz- und Basisnote. Riech doch einfach mal rein!
Mein Logo ist zu verwenden.
Einige Kurzgeschichten aus dem Buch stehen auf meiner Website, zum Reinlesen bei Bedarf.
Die Katastrophe, der Wendepunkt in meinem Leben, war der Tod meines Mannes.
Meine Website lautet : www.baum-feldner.de

```html
<!DOCTYPE html>
<html lang="de">
<head>
<meta charset="utf-8">
<title>Sturmflut im Herbstlicht – Lena Baumfeld</title>
<link rel="stylesheet" href="https://fonts.googleapis.com/css2?family=Source+Serif+4:opsz,wght@8..60,400;8..60,600&display=swap">
<style>
  :root {
    --paper: #fdfdfd;
    --brand-red: #a4283a;
    --ink: #333133;
    --sky: #9fb8d4;
    --stone: #c9cfd6;
    --hoodie: #b0112f;
    --lawn: #c8dc98;
  }
  * { margin: 0; padding: 0; box-sizing: border-box; }
  html, body {
    width: 850px;
    height: 1200px;
    overflow: hidden;
    background: var(--paper);
  }
  .cover {
    position: relative;
    width: 850px;
    height: 1200px;
    background: var(--paper);
    font-family: "Source Serif 4", Georgia, serif;
    color: var(--ink);
  }
  .brand {
    position: absolute;
    top: 70px;
    left: 0;
    width: 100%;
    display: flex;
    flex-direction: column;
    align-items: center;
    gap: 22px;
  }
  .brand-mark {
    width: 64px;
    height: 64px;
    border: 2px solid var(--brand-red);
    border-radius: 50%;
  }
  .brand-name {
    font-size: 30px;
    font-weight: 400;
    color: var(--brand-red);
    letter-spacing: 0.02em;
  }
  .initial {
    position: absolute;
    top: 290px;
    left: 0;
    width: 850px;
    height: 570px;
  }
  .author {
    position: absolute;
    top: 880px;
    left: 0;
    width: 100%;
    text-align: center;
    font-size: 33px;
    font-weight: 400;
    letter-spacing: 0.12em;
    color: var(--brand-red);
    text-transform: uppercase;
  }
  .title {
    position: absolute;
    top: 935px;
    left: 0;
    width: 100%;
    text-align: center;
    font-size: 104px;
    font-weight: 400;
    line-height: 104px;
    letter-spacing: -0.01em;
    color: var(--ink);
  }
</style>
</head>
<body>
  <main class="cover">
    <header class="brand">
      <span class="brand-mark"></span>
      <span class="brand-name">Lena Baumfeld</span>
    </header>

    <svg class="initial" viewBox="0 0 850 570" role="img" aria-label="Großes Initial S, gefüllt mit einem Porträtfoto der Autorin im roten Kapuzenpullover vor Hauswand, Himmel und Wiese">
      <defs>
        <linearGradient id="portrait-fill" x1="0" y1="0" x2="0.4" y2="1">
          <stop offset="0" stop-color="var(--sky)"/>
          <stop offset="0.28" stop-color="var(--stone)"/>
          <stop offset="0.5" stop-color="var(--hoodie)"/>
          <stop offset="0.82" stop-color="var(--hoodie)"/>
          <stop offset="1" stop-color="var(--lawn)"/>
        </linearGradient>
      </defs>
      <text x="425" y="555" text-anchor="middle" font-family="'Source Serif 4', Georgia, serif" font-weight="600" font-size="790" fill="url(#portrait-fill)">S</text>
    </svg>

    <p class="author">Lena Baumfeld</p>
    <h1 class="title">Sturmflut<br>im Herbstlicht</h1>
  </main>
</body>
</html>
```